Half page (a5) ad for a company

I need a design for an ad for a company to be published in a conference catalogue. Please find enclosed the logo for a company. The company is providing health screening services. Ad should be subtle and minimalistic, i.e. logo in the centre and a phrase saying: "Be in charge of your own health" and the website vantolix.co.uk. Also please find enclosed guidlines for colours and fonts to be used.

```html
<!DOCTYPE html>
<html lang="en">
<head>
<meta charset="utf-8">
<title>Vantolix Health – A5 Ad</title>
<link rel="stylesheet" href="https://fonts.googleapis.com/css2?family=Montserrat:wght@400;600&display=swap">
<style>
  :root {
    --backdrop: #e0e0e0;
    --ink: #000000;
    --brand-red: #e30613;
    --brand-red-deep: #a50d18;
    --paper-text: #ffffff;
  }
  * { margin: 0; padding: 0; box-sizing: border-box; }
  html, body {
    width: 1200px;
    height: 1200px;
    overflow: hidden;
    background: var(--backdrop);
  }
  .ad {
    position: absolute;
    left: 176px;
    top: 0;
    width: 848px;
    height: 1200px;
    background: var(--ink);
    font-family: "Montserrat", sans-serif;
    text-align: center;
  }
  .brand {
    position: absolute;
    left: 0;
    right: 0;
    top: 200px;
    display: flex;
    flex-direction: column;
    align-items: center;
  }
  .brand-dot {
    width: 120px;
    height: 120px;
    border-radius: 50%;
    background: var(--brand-red);
  }
  .brand-name {
    margin-top: 120px;
    font-size: 70px;
    font-weight: 400;
    line-height: 1;
    color: var(--brand-red);
    letter-spacing: -0.5px;
  }
  .tagline {
    position: absolute;
    left: 0;
    right: 0;
    top: 738px;
    font-size: 60px;
    font-weight: 600;
    line-height: 74px;
    letter-spacing: 0.5px;
  }
  .tagline-lead { display: block; color: var(--paper-text); }
  .tagline-accent { display: block; color: var(--brand-red); }
  .web-button {
    position: absolute;
    left: 50%;
    top: 1019px;
    transform: translateX(-50%);
    width: 282px;
    height: 60px;
    border-radius: 30px;
    background: linear-gradient(180deg, var(--brand-red) 55%, var(--brand-red-deep) 100%);
    color: var(--paper-text);
    font-size: 29px;
    font-weight: 600;
    line-height: 60px;
    letter-spacing: 0.3px;
  }
</style>
</head>
<body>
  <main class="ad">
    <div class="brand">
      <span class="brand-dot"></span>
      <p class="brand-name">Vantolix Health</p>
    </div>
    <h1 class="tagline">
      <span class="tagline-lead">Be in charge of</span>
      <span class="tagline-accent">your own health</span>
    </h1>
    <p class="web-button">vantolix.co.uk</p>
  </main>
</body>
</html>
```